Wealth Education Business Needs Sharp Business Card Design

We need a business card design for a recently launched investor education business called Harbor Crest.

The final design should promote security, empowerment, self improvement and financial gain. The card will ideally promote the stature of the business.

For more information and colours please visit harborcrest.com.au

Target Market(s)

Corporate executives and high net worth individuals

Industry/Entity Type

Education

Contact Information for Business Card

Name
Position
Contact Address
Phone
Mobile
Email
Website

```html
<!DOCTYPE html>
<html lang="en">
<head>
<meta charset="utf-8">
<title>Harbor Crest – Business Card</title>
<link rel="stylesheet" href="https://fonts.googleapis.com/css2?family=Oswald:wght@400;600&family=Open+Sans:wght@400;600&display=swap">
<style>
  :root {
    --navy: #1b2a3c;
    --teal: #1f8b8f;
    --teal-light: #3fb3b0;
    --ink: #333a40;
    --muted: #6d7780;
    --paper: #ffffff;
    --backdrop: #e9e7e3;
  }
  * { margin: 0; padding: 0; box-sizing: border-box; }
  html, body { width: 1200px; height: 902px; overflow: hidden; }
  body {
    background: var(--backdrop);
    display: flex;
    align-items: center;
    justify-content: center;
    gap: 40px;
    font-family: "Open Sans", Arial, sans-serif;
  }
  .card {
    position: relative;
    width: 540px;
    height: 310px;
    border-radius: 14px;
    box-shadow: 0 10px 26px rgba(0,0,0,0.18);
    overflow: hidden;
  }

  /* Front */
  .card--front { background: var(--navy); }
  .front-lockup {
    position: absolute;
    left: 110px;
    top: 104px;
    display: flex;
    align-items: center;
    gap: 18px;
  }
  .brand-dot {
    width: 58px; height: 58px;
    border-radius: 50%;
    background: var(--teal-light);
  }
  .front-name {
    font-family: "Oswald", "Arial Narrow", sans-serif;
    font-weight: 600;
    font-size: 40px;
    letter-spacing: 2px;
    color: #ffffff;
    line-height: 1;
  }
  .front-tagline {
    margin-top: 6px;
    font-family: "Oswald", "Arial Narrow", sans-serif;
    font-weight: 400;
    font-size: 14px;
    letter-spacing: 6px;
    color: var(--teal-light);
    white-space: nowrap;
  }
  .front-web {
    position: absolute;
    left: 0; right: 0;
    top: 232px;
    text-align: center;
    font-size: 13px;
    color: #8795a3;
    letter-spacing: 0.5px;
  }

  /* Back */
  .card--back { background: var(--paper); }
  .back-lockup {
    position: absolute;
    left: 150px;
    top: 52px;
    display: flex;
    align-items: center;
    gap: 12px;
  }
  .back-lockup .brand-dot { width: 34px; height: 34px; background: var(--teal); }
  .back-name {
    font-family: "Oswald", "Arial Narrow", sans-serif;
    font-weight: 600;
    font-size: 28px;
    letter-spacing: 3px;
    color: var(--ink);
  }
  .address {
    position: absolute;
    right: 34px;
    top: 106px;
    text-align: right;
    font-style: normal;
    font-size: 13px;
    line-height: 1.45;
    color: var(--ink);
  }
  .divider {
    position: absolute;
    left: 148px;
    right: 34px;
    top: 168px;
    height: 1.5px;
    background: var(--teal);
  }
  .person {
    position: absolute;
    left: 34px;
    top: 156px;
  }
  .person-name {
    font-family: "Oswald", "Arial Narrow", sans-serif;
    font-weight: 600;
    font-size: 17px;
    letter-spacing: 0.5px;
    color: var(--ink);
    line-height: 1.2;
  }
  .person-name .first { color: var(--teal); }
  .person-title { font-size: 13px; color: var(--ink); }
  .contacts {
    position: absolute;
    left: 34px;
    top: 210px;
    list-style: none;
  }
  .contacts li {
    display: flex;
    align-items: center;
    gap: 10px;
    font-size: 13px;
    color: var(--ink);
    line-height: 21px;
  }
  .contacts svg { width: 11px; height: 11px; fill: var(--ink); flex: none; }
</style>
</head>
<body>

  <section class="card card--front" aria-label="Card front">
    <div class="front-lockup">
      <span class="brand-dot"></span>
      <div>
        <div class="front-name">HARBOR CREST</div>
        <div class="front-tagline">STUDY BUILD FLOURISH</div>
      </div>
    </div>
    <p class="front-web">www.harborcrest.com.au</p>
  </section>

  <section class="card card--back" aria-label="Card back">
    <div class="back-lockup">
      <span class="brand-dot"></span>
      <span class="back-name">HARBOR CREST</span>
    </div>

    <address class="address">
      Level 3, 42 Quayside Walk<br>
      Dockland VIC 3010
    </address>

    <div class="divider"></div>

    <div class="person">
      <div class="person-name"><span class="first">YOUR</span> NAME</div>
      <div class="person-title">Title</div>
    </div>

    <ul class="contacts">
      <li>
        <svg viewBox="0 0 12 12" aria-hidden="true"><path d="M2.5 0.8l2 2-1 1.4c.6 1.3 1.7 2.4 3 3l1.4-1 2 2-1.3 2C5 10 2 7 0.8 2.1z"/></svg>
        1300 555 218
      </li>
      <li>
        <svg viewBox="0 0 12 12" aria-hidden="true"><path d="M1 1h10v8H1zM2 2v6h8V2zM3 10h6v1.2H3z"/></svg>
        +613 5550 4172
      </li>
      <li>
        <svg viewBox="0 0 12 12" aria-hidden="true"><path d="M0.5 2h11v8h-11zM1.5 3v.3L6 6.5l4.5-3.2V3zM1.5 4.5V9h9V4.5L6 7.7z"/></svg>
        support@harborcrest.com.au
      </li>
      <li>
        <svg viewBox="0 0 12 12" aria-hidden="true"><circle cx="6" cy="6" r="5.3" fill="none" stroke="#333a40" stroke-width="1.1"/><path d="M0.8 6h10.4M6 0.8v10.4" stroke="#333a40" stroke-width="0.9"/><ellipse cx="6" cy="6" rx="2.4" ry="5.2" fill="none" stroke="#333a40" stroke-width="0.9"/></svg>
        www.harborcrest.com.au
      </li>
    </ul>
  </section>

</body>
</html>
```